Do i have coronavirus, flue or cold?

Using information from PFA and government agencies we want to make a easy to read infographic helping patients see if they have coronavirus, the flu or a cold. Using a flow diagram or whatever you think will make it easy to read and digest for the average lamen.

Information is in the word document and in the chart.

We are www.calvexa.co.uk attached is our brand guidelines, we will be putting this infographic on our website and email/sms it to all of our 300,000 patients.

```html
<!DOCTYPE html>
<html lang="en">
<head>
<meta charset="utf-8">
<title>Do I have coronavirus, flue or cold?</title>
<link rel="stylesheet" href="https://fonts.googleapis.com/css2?family=Roboto+Condensed:ital,wght@0,700;0,900;1,700;1,900&display=swap">
<style>
  :root {
    --navy: #05053a;
    --orange: #f55f1f;
    --flu-blue: #6b8cf0;
    --peach: #ffa37f;
    --symptom-blue: #3535b8;
    --frame-grey: #c9c9c9;
    --cell-white: #ffffff;
    --cell-grey: #f2f2f2;
    --rule: #b8b8c8;
    --icon-tone: #c9d6f5;
  }
  * { box-sizing: border-box; margin: 0; padding: 0; }
  html, body { width: 926px; height: 1200px; overflow: hidden; background: var(--frame-grey); }
  body { font-family: "Roboto Condensed", "Arial Narrow", sans-serif; color: var(--navy); }

  .poster { width: 926px; height: 1200px; background: var(--frame-grey); display: flex; flex-direction: column; }

  .title-band {
    height: 86px; background: var(--navy);
    display: flex; align-items: center; justify-content: center;
    font-weight: 700; font-size: 46px; letter-spacing: -1px; color: #fff;
    border-bottom: 3px solid #fff;
  }
  .title-band .t-corona { color: var(--orange); }
  .title-band .t-flu { color: var(--flu-blue); }
  .title-band .t-cold { color: var(--peach); margin-left: 10px; }
  .title-band .t-gap { margin-left: 10px; }

  .column-heads {
    display: grid; grid-template-columns: 301px 239px 173px 213px; height: 72px;
  }
  .column-heads div {
    display: flex; align-items: center; justify-content: center;
    font-style: italic; font-weight: 700; font-size: 33px; color: #fff;
  }
  .head-symptom { background: var(--symptom-blue); }
  .head-corona { background: var(--orange); }
  .head-flu { background: var(--flu-blue); }
  .head-cold { background: var(--peach); }

  .chart {
    margin: 0 16px 0 17px; flex: 1 0 auto; max-height: 1017px;
    display: grid; grid-template-columns: 284px 239px 173px 197px;
    grid-auto-rows: 1fr; background: var(--cell-white);
    border-radius: 0 0 14px 14px; overflow: hidden;
  }
  .cell {
    display: flex; align-items: center; justify-content: center; flex-direction: column;
    border-bottom: 2px solid var(--rule); border-right: 2px solid var(--rule);
    background: var(--cell-white); text-align: center; line-height: 1;
  }
  .cell:nth-child(4n) { border-right: none; }
  .chart > .cell:nth-last-child(-n+4) { border-bottom: none; }
  .cell.muted { background: var(--cell-grey); }

  .symptom { flex-direction: row; justify-content: flex-start; padding-left: 28px; gap: 20px; text-align: left; }
  .symptom-icon { width: 72px; height: 76px; flex: none; display: block; }
  .symptom-name { font-weight: 700; font-size: 21px; line-height: 1.15; }

  .answer-yes { font-weight: 700; font-size: 60px; letter-spacing: -1px; transform: scaleY(1.05); }
  .answer-word { font-weight: 700; font-size: 27px; }
  .answer-note { font-weight: 700; font-size: 17px; color: var(--orange); margin-top: 2px; }
  .cold .answer-word { font-size: 26px; }
  .flu .answer-word { font-size: 25px; }
  .chart-foot { height: 25px; }
</style>
</head>
<body>
<main class="poster">
  <header class="title-band">
    <h1 style="font:inherit">DO I HAVE <span class="t-corona">CORONAVIRUS</span>, <span class="t-flu">FLUE</span><span class="t-gap">OR</span><span class="t-cold">COLD?</span></h1>
  </header>

  <div class="column-heads">
    <div class="head-symptom">SYMPTOM</div>
    <div class="head-corona">CORONAVIRUS</div>
    <div class="head-flu">FLU</div>
    <div class="head-cold">COLD</div>
  </div>

  <section class="chart">
    <!-- Fever -->
    <div class="cell symptom"><svg class="symptom-icon" role="img" aria-label="Illustration of a person with a fever and a thermometer"><rect width="72" height="76" rx="8" fill="var(--icon-tone)"/></svg><span class="symptom-name">FEVER</span></div>
    <div class="cell corona"><span class="answer-yes">YES</span></div>
    <div class="cell flu"><span class="answer-yes">YES</span><span class="answer-note">HIGH</span></div>
    <div class="cell cold muted"><span class="answer-word">RARE</span></div>

    <!-- Cough -->
    <div class="cell symptom"><svg class="symptom-icon" role="img" aria-label="Illustration of a person coughing"><rect width="72" height="76" rx="8" fill="var(--icon-tone)"/></svg><span class="symptom-name">COUGH</span></div>
    <div class="cell corona"><span class="answer-yes">YES</span><span class="answer-note">DRY COUGH</span></div>
    <div class="cell flu"><span class="answer-yes">YES</span></div>
    <div class="cell cold muted"><span class="answer-word">MODERATE</span></div>

    <!-- Tiredness -->
    <div class="cell symptom"><svg class="symptom-icon" role="img" aria-label="Illustration of a tired person"><rect width="72" height="76" rx="8" fill="var(--icon-tone)"/></svg><span class="symptom-name">TIREDNESS</span></div>
    <div class="cell corona"><span class="answer-yes">YES</span></div>
    <div class="cell flu"><span class="answer-yes">YES</span></div>
    <div class="cell cold muted"><span class="answer-word">MILD</span></div>

    <!-- Shortness of breath -->
    <div class="cell symptom"><svg class="symptom-icon" role="img" aria-label="Illustration of a person short of breath"><rect width="72" height="76" rx="8" fill="var(--icon-tone)"/></svg><span class="symptom-name">SHORTNESS<br>OF BREATH</span></div>
    <div class="cell corona"><span class="answer-yes">YES</span></div>
    <div class="cell flu"><span class="answer-yes">YES</span></div>
    <div class="cell cold muted"><span class="answer-word">RARE</span></div>

    <!-- Muscle aches -->
    <div class="cell symptom"><svg class="symptom-icon" role="img" aria-label="Illustration of a person with muscle aches"><rect width="72" height="76" rx="8" fill="var(--icon-tone)"/></svg><span class="symptom-name">MUSCLE<br>ACHES</span></div>
    <div class="cell corona"><span class="answer-yes">YES</span></div>
    <div class="cell flu"><span class="answer-yes">YES</span><span class="answer-note">OFTEN</span></div>
    <div class="cell cold muted"><span class="answer-word">MODERATE</span></div>

    <!-- Headache -->
    <div class="cell symptom"><svg class="symptom-icon" role="img" aria-label="Illustration of a person with a headache"><rect width="72" height="76" rx="8" fill="var(--icon-tone)"/></svg><span class="symptom-name">HEADACHE</span></div>
    <div class="cell corona muted"><span class="answer-word">SOMETIMES</span></div>
    <div class="cell flu"><span class="answer-yes">YES</span></div>
    <div class="cell cold muted"><span class="answer-word">RARE</span></div>

    <!-- Sore throat -->
    <div class="cell symptom"><svg class="symptom-icon" role="img" aria-label="Illustration of a person with a sore throat"><rect width="72" height="76" rx="8" fill="var(--icon-tone)"/></svg><span class="symptom-name">SORE<br>THROAT</span></div>
    <div class="cell corona muted"><span class="answer-word">SOMETIMES</span></div>
    <div class="cell flu muted"><span class="answer-word">SOMETIMES</span></div>
    <div class="cell cold"><span class="answer-yes">YES</span></div>

    <!-- Stuffy or runny nose -->
    <div class="cell symptom"><svg class="symptom-icon" role="img" aria-label="Illustration of a person with a runny nose"><rect width="72" height="76" rx="8" fill="var(--icon-tone)"/></svg><span class="symptom-name">STUFFY OR<br>RUNNY NOSE</span></div>
    <div class="cell corona muted"><span class="answer-word">RARE</span></div>
    <div class="cell flu muted"><span class="answer-word">SOMETIMES</span></div>
    <div class="cell cold"><span class="answer-yes">YES</span></div>

    <!-- Sneezing -->
    <div class="cell symptom"><svg class="symptom-icon" role="img" aria-label="Illustration of a person sneezing"><rect width="72" height="76" rx="8" fill="var(--icon-tone)"/></svg><span class="symptom-name">SNEEZING</span></div>
    <div class="cell corona muted"><span class="answer-word">NO</span></div>
    <div class="cell flu muted"><span class="answer-word">SOMETIMES</span></div>
    <div class="cell cold"><span class="answer-yes">YES</span></div>
  </section>
  <div class="chart-foot"></div>
</main>
</body>
</html>
```